Business Card Design for Varnok Facility Services

We are looking for a Business Card Design for the Company "Varnok Facility Services."
Front side:
- Company Logo (small)
- Company Name, address, pohone, website and personal data.
- white background, for text e.g. company colors (blue or green like in the logo)
Please use following data:
Company data:
Varnok Facility Services Tulbrecht
Kirchmattweg 12
6331 Cham
www.varnok-fs.ch
Person data:
Ruben Tulbrecht
Geschäftsführer
+41 76 519 84 60
info@varnok-fs.ch
Back side:
could be colored in blue or green
please use a big logo sing and some smaller icons to say what is all beeing offered in facility services, like cleaning, maintenance cleaning
industrial cleaning, caretaking, gardening, disposal. There is no need for everyone of the icons if there are similar or an icon is standing for more of them.
Cleaning Service
colors to use:
blue: HEX 246BB0
green: HEX 52B33E

```html
<!DOCTYPE html>
<html lang="de">
<head>
<meta charset="utf-8">
<title>Varnok Facility Services – Business Card</title>
<link rel="stylesheet" href="https://fonts.googleapis.com/css2?family=Roboto:wght@400;500;700;900&display=swap">
<style>
  :root {
    --brand-blue: #246BB0;
    --brand-green: #17A83B;
    --light-blue: #8EC8FF;
    --band-dark: #3C3C3C;
    --paper: #FFFFFF;
    --stage: #E9E9E9;
  }
  * { margin: 0; padding: 0; box-sizing: border-box; }
  html, body { width: 1200px; height: 1200px; overflow: hidden; background: var(--stage); }
  body { font-family: "Roboto", sans-serif; position: relative; }

  .card {
    position: absolute;
    left: 190px;
    width: 820px;
    height: 469px;
    border-radius: 28px;
    overflow: hidden;
    box-shadow: 0 10px 30px rgba(0,0,0,.18);
  }

  /* Back side */
  .card--back { top: 100px; background: var(--brand-blue); color: var(--paper); }
  .back-brand {
    position: absolute; top: 70px; left: 0; right: 0;
    display: flex; flex-direction: column; align-items: center; gap: 18px;
  }
  .brand-dot { width: 70px; height: 70px; border-radius: 50%; background: var(--paper); }
  .back-brand .brand-name {
    font-weight: 700; font-size: 46px; letter-spacing: 2px; text-transform: uppercase; color: var(--paper);
  }
  .services {
    position: absolute; bottom: 40px; left: 0; right: 0;
    display: flex; justify-content: center; gap: 44px;
  }
  .service { display: flex; flex-direction: column; align-items: center; width: 120px; }
  .service-icon {
    width: 86px; height: 86px; border-radius: 50%;
    border: 3px solid var(--paper);
    background: var(--paper);
    box-shadow: inset 0 0 0 4px var(--brand-blue);
  }
  .service-label {
    margin-top: 10px; font-size: 13px; font-weight: 700; text-transform: uppercase;
    text-align: center; line-height: 1.05;
  }

  /* Front side */
  .card--front { top: 630px; background: var(--paper); }
  .front-panel { position: absolute; inset: 0; }
  .name-band {
    position: absolute; left: 30px; top: 50px; width: 440px; height: 78px;
    background: var(--brand-green); color: var(--paper);
    display: flex; align-items: center; padding-left: 48px;
    font-weight: 900; font-size: 30px; text-transform: uppercase; letter-spacing: .5px;
  }
  .role-band {
    position: absolute; left: 478px; top: 140px; width: 318px; height: 64px;
    background: var(--band-dark); color: var(--paper);
    display: flex; align-items: center; justify-content: center;
    font-size: 24px; letter-spacing: 2px;
  }
  .front-brand {
    position: absolute; left: 50px; top: 290px;
    display: flex; align-items: center; gap: 16px;
  }
  .front-brand .brand-dot { width: 44px; height: 44px; background: var(--brand-blue); }
  .front-brand .brand-name {
    font-weight: 700; font-size: 30px; color: var(--brand-blue); text-transform: uppercase; line-height: 1.1;
  }
  .contact {
    position: absolute; left: 470px; top: 300px; color: var(--paper);
  }
  .contact-company { font-weight: 700; font-size: 19px; color: var(--light-blue); }
  .contact-address { font-size: 19px; line-height: 1.25; margin-bottom: 12px; }
  .contact-line { display: flex; align-items: center; gap: 10px; font-size: 19px; line-height: 1.4; }
  .contact-line svg { width: 18px; height: 18px; flex: none; }
  .contact-line strong { font-weight: 700; }
</style>
</head>
<body>

<section class="card card--back" aria-label="Card back">
  <div class="back-brand">
    <span class="brand-dot"></span>
    <span class="brand-name">Varnok Facility Services</span>
  </div>
  <ul class="services" style="list-style:none">
    <li class="service">
      <span class="service-icon" role="img" aria-label="Cleaning brush icon"></span>
      <span class="service-label">Maintenance<br>Cleaning</span>
    </li>
    <li class="service">
      <span class="service-icon" role="img" aria-label="Handshake with heart icon"></span>
      <span class="service-label">Caretaking</span>
    </li>
    <li class="service">
      <span class="service-icon" role="img" aria-label="Flower pot icon"></span>
      <span class="service-label">Gardening</span>
    </li>
    <li class="service">
      <span class="service-icon" role="img" aria-label="Waste bin icon"></span>
      <span class="service-label">Disposal</span>
    </li>
  </ul>
</section>

<section class="card card--front" aria-label="Card front">
  <svg class="front-panel" viewBox="0 0 820 469" preserveAspectRatio="none" aria-hidden="true">
    <polygon points="505,0 820,0 820,469 385,469" fill="var(--brand-blue)"/>
  </svg>

  <div class="name-band">Ruben Tulbrecht</div>
  <div class="role-band">Geschäftsführer</div>

  <div class="front-brand">
    <span class="brand-dot"></span>
    <span class="brand-name">Varnok<br>Facility Services</span>
  </div>

  <div class="contact">
    <p class="contact-company">Varnok Facility Services Tulbrecht</p>
    <p class="contact-address">Kirchmattweg 12<br>6331 Cham</p>
    <p class="contact-line">
      <svg viewBox="0 0 24 24" aria-hidden="true"><path fill="#fff" d="M6.6 10.8a15 15 0 0 0 6.6 6.6l2.2-2.2a1 1 0 0 1 1-.25 11.4 11.4 0 0 0 3.6.57 1 1 0 0 1 1 1V20a1 1 0 0 1-1 1A17 17 0 0 1 3 4a1 1 0 0 1 1-1h3.5a1 1 0 0 1 1 1c0 1.25.2 2.45.57 3.57a1 1 0 0 1-.25 1z"/></svg>
      +41 76 519 84 60
    </p>
    <p class="contact-line">
      <svg viewBox="0 0 24 24" aria-hidden="true"><rect x="3" y="5" width="18" height="14" rx="1.5" fill="none" stroke="#fff" stroke-width="2"/><path d="M3 6l9 7 9-7" fill="none" stroke="#fff" stroke-width="2"/></svg>
      info@varnok-fs.ch
    </p>
    <p class="contact-line">
      <svg viewBox="0 0 24 24" aria-hidden="true"><g fill="none" stroke="#fff" stroke-width="1.8"><circle cx="12" cy="12" r="9"/><ellipse cx="12" cy="12" rx="4" ry="9"/><path d="M3 12h18M5 7h14M5 17h14"/></g></svg>
      <span>www.<strong>varnok-fs</strong>.ch</span>
    </p>
  </div>
</section>

</body>
</html>
```